Website Needs a New Look & Feel - I am Too Old and Uncool on my Own

I want some design ideas for my current site. I need a new, more modern and dynamic look and feel. The audience for the site is 90% male, 24-54 years old, and not highly educated. English is second language for about 30% of audience, so images help. 85% of visitors view on mobile. We sell trucks and trailers to this audience. . Just want something new and cool. Tired of what I have. Current site doesn't seem strong enough to match the kind of people who drive trucks for a living. Current is site is brelvon.com. Pull relevant menu and text from the site.

Target Market(s)

Truck Drivers and Trucking Company Owners (90% male).

Industry/Entity Type

Transportation - Specifically, truck and trailer sales.

Number of Pages Required

3 page

Font styles to use
Sans Serif

Colors
0054AA
0677BA
7BADD7
CADEEF
E8F1F8

Requirements
Must have
• Images of Sleeper Trucks (like on there now) and trailers. Audience is very literal, so they need to see what we sell.
Nice to have
• Images of Sleeper Trucks (like on tMy inventory pages are boring, please show me something more user-friendly and interesting. here now) and trailers.

```html
<!DOCTYPE html>
<html lang="en">
<head>
<meta charset="utf-8">
<title>Brelvon Truck &amp; Trailer — Buy Like a Fleet</title>
<link rel="stylesheet" href="https://fonts.googleapis.com/css2?family=Montserrat:wght@500;600;700;800&family=Open+Sans:wght@400;600;700&display=swap">
<style>
:root{
  --navy:#14215a;
  --navy-deep:#0e1845;
  --blue:#0054AA;
  --blue-mid:#0677BA;
  --blue-soft:#7BADD7;
  --blue-pale:#CADEEF;
  --blue-mist:#E8F1F8;
  --ink:#1d2340;
  --text:#3a3f55;
  --white:#ffffff;
}
*{box-sizing:border-box;margin:0;padding:0}
html,body{width:1200px;height:4848px;overflow:hidden}
body{position:relative;background:var(--white);font-family:"Open Sans",Arial,sans-serif;color:var(--text)}
.abs{position:absolute}
h1,h2,h3,.btn,.nav a,.brand{font-family:"Montserrat",Arial,sans-serif}
.btn{display:inline-flex;align-items:center;justify-content:center;font-size:15px;font-weight:700;letter-spacing:1.5px;text-transform:uppercase;text-decoration:none;white-space:nowrap}
.btn-navy{background:var(--navy);color:var(--white)}
.btn-ghost{border:2px solid var(--white);color:var(--white)}

/* header */
.site-header{left:0;top:0;width:1200px;height:92px;background:var(--white);z-index:3}
.brand{left:88px;top:14px;color:var(--navy);line-height:1}
.brand .name{font-size:40px;font-weight:800;letter-spacing:1px;display:block}
.brand .sub{font-size:19px;font-weight:600;display:block;margin-top:2px}
.nav{left:400px;top:38px;display:flex;gap:18px}
.nav a{font-size:14px;font-weight:600;color:var(--ink);text-decoration:none;white-space:nowrap}
.header-cta{left:890px;top:24px;width:240px;height:48px;font-size:13px}

/* hero */
.hero{left:0;top:92px;width:1200px;height:968px;background:linear-gradient(180deg,#1c2f7a 0%,#14215a 70%,#101a4c 100%);overflow:hidden}
.hero-photo{left:560px;top:0;width:640px;height:520px;background:linear-gradient(100deg,#2a3f8a 0%,#8c9ab8 45%,#d7dde7 70%,#b9c3d4 100%)}
.hero-slant{left:0;top:0;width:1200px;height:520px}
.hero-kicker{left:88px;top:180px;font-family:"Montserrat",sans-serif;font-size:26px;font-weight:600;letter-spacing:5px;color:var(--white)}
.hero-title{left:88px;top:222px;font-size:50px;font-weight:800;letter-spacing:2px;color:var(--white)}
.hero-inv{left:88px;top:332px;width:232px;height:52px}
.hero-phone{left:348px;top:342px;display:flex;align-items:center;gap:10px;color:var(--white);font-weight:700;font-size:17px;font-family:"Montserrat",sans-serif}
.cats{left:88px;top:528px;display:flex;gap:24px}
.cat{position:relative;width:240px;height:360px;border:3px solid var(--white);background:var(--white)}
.cat-photo{position:absolute;inset:6px 6px 56px 6px}
.cat-label{position:absolute;left:6px;right:6px;bottom:6px;height:44px;background:var(--navy);color:var(--white);display:flex;align-items:center;justify-content:space-between;padding:0 14px;font-family:"Montserrat",sans-serif;font-weight:700;font-size:16px;letter-spacing:1px}

/* section headings with square accent */
.accent-title{font-family:"Montserrat",sans-serif;font-weight:800;color:var(--navy);text-transform:uppercase;line-height:1.15}
.accent-title .sq{display:inline-block;width:44px;height:44px;background:var(--blue);vertical-align:-6px;margin-right:-30px}
.accent-title .first{position:relative}

/* wholesale */
.wholesale-bg{left:0;top:1088px;width:1200px;height:632px;background:var(--blue-mist)}
.wholesale-photo{left:0;top:1088px;width:500px;height:592px;background:linear-gradient(135deg,#e6e9ef 0%,#b8bfcc 45%,#6f7890 100%)}
.wholesale-text{left:600px;top:1120px;width:520px}
.wholesale-text h2{font-size:40px}
.wholesale-text p{margin-top:24px;font-size:15px;line-height:1.75}
.wholesale-btn{left:600px;top:1528px;width:172px;height:52px}

/* buying */
.buying-head{left:0;top:1810px;width:1200px;text-align:center}
.buying-head h2{font-size:44px}
.buying-lead{left:240px;top:1938px;width:720px;text-align:center;font-size:15px;line-height:1.75}
.why-title{left:88px;top:2068px;font-family:"Montserrat",sans-serif;font-weight:800;font-size:22px;color:var(--ink)}
.why-list{left:88px;top:2130px;width:500px}
.why-item{display:flex;align-items:center;height:90px;margin-bottom:18px}
.why-icon{width:56px;height:56px;background:var(--navy);display:flex;align-items:center;justify-content:center;flex:none}
.why-box{margin-left:18px;width:370px;border:2px solid var(--navy);padding:12px 16px;font-size:14px;line-height:1.6;color:var(--ink)}
.buying-photo{left:604px;top:2040px;width:488px;height:440px;background:linear-gradient(180deg,#2d4da0 0%,#5d7ac0 40%,#d4a36b 72%,#3a3f55 100%)}
.mission{left:80px;top:2500px;width:1120px;height:250px;background:var(--blue-mist)}
.mission p{position:absolute;left:170px;top:58px;width:780px;text-align:center;font-size:15px;line-height:1.75}

/* sell band */
.sell-band{left:0;top:2750px;width:1200px;height:630px;background:linear-gradient(90deg,#6f84c4 0%,#34509e 45%,#1b2f7c 100%)}
.sell-title{left:600px;top:2990px;width:560px;font-size:52px;font-weight:800;color:var(--white);line-height:1.15;text-transform:uppercase}
.sell-btn{left:600px;top:3240px;width:260px;height:52px;font-size:14px}

/* resources */
.res-head{left:0;top:3456px;width:1200px;text-align:center}
.res-head h2{font-size:40px}
.res-cards{left:148px;top:3540px;display:flex;gap:22px}
.res-card{width:284px;height:380px;background:var(--white);box-shadow:0 6px 20px rgba(20,33,90,.12)}
.res-photo{height:250px}
.res-card h3{padding:18px 18px 0;font-size:22px;font-weight:800;color:var(--navy);line-height:1.2;text-transform:uppercase}
.res-arrow{top:3704px;width:56px;height:56px;border:2px solid var(--navy);background:var(--white);display:flex;align-items:center;justify-content:center}

/* contact */
.contact-bg{left:40px;top:4000px;width:1160px;height:520px;background:var(--blue-mist)}
.contact-head{left:160px;top:4096px;width:380px}
.contact-head h2{font-size:38px}
.contact-head p{margin-top:22px;font-size:14px;line-height:1.7}
.contact-line{left:160px;display:flex;align-items:center;gap:18px}
.contact-line .ico{width:40px;height:40px;border:2px solid var(--navy);display:flex;align-items:center;justify-content:center}
.contact-line small{display:block;font-size:12px;font-weight:700;letter-spacing:1.5px;color:var(--ink)}
.contact-line strong{font-family:"Montserrat",sans-serif;font-size:20px;color:var(--navy)}
.form-card{left:592px;top:4076px;width:508px;height:500px;background:var(--white);box-shadow:0 10px 30px rgba(20,33,90,.15);padding:36px 32px;z-index:2}
.form-card h3{font-size:22px;font-weight:800;color:var(--ink);letter-spacing:1px}
.field-row{display:flex;gap:16px;margin-top:20px}
.field{flex:1;height:46px;border-bottom:1px solid var(--blue-pale);display:flex;align-items:center;gap:10px;font-size:13px;color:#7a8098;padding-left:6px}
.field i{width:12px;height:12px;background:var(--blue-soft);display:inline-block}
.form-btn{margin-top:44px;width:172px;height:52px}

/* footer */
.site-footer{left:0;top:4520px;width:1200px;height:328px;background:var(--navy-deep)}
.foot-brand{left:100px;top:4586px;color:var(--white)}
.foot-nav{left:470px;top:4628px;display:flex;gap:32px}
.foot-nav a{color:var(--white);font-family:"Montserrat",sans-serif;font-size:14px;text-decoration:none}
.foot-rule{left:100px;top:4720px;width:1000px;height:1px;background:rgba(255,255,255,.25)}
.social{left:100px;top:4748px;display:flex;gap:10px}
.social span{width:30px;height:30px;background:rgba(255,255,255,.2)}
.copy{left:0;top:4790px;width:1200px;text-align:center;color:var(--white);font-size:13px}
.policy{left:1016px;top:4790px;color:var(--white);font-size:13px}
</style>
</head>
<body>

<header class="abs site-header">
  <div class="abs brand"><span class="name">BRELVON</span><span class="sub">Truck &amp; Trailer</span></div>
  <nav class="abs nav"><a href="#">Sleepers</a><a href="#">Reefers</a><a href="#">Dry Vans</a><a href="#">Cranes</a><a href="#">Resources</a><a href="#">Contact</a></nav>
  <a class="abs btn btn-navy header-cta" href="#">See Our Inventory</a>
</header>

<section class="abs hero">
  <div class="abs hero-photo" role="img" aria-label="Row of white semi trucks parked at a depot"></div>
  <svg class="abs hero-slant" viewBox="0 0 1200 520" preserveAspectRatio="none" aria-hidden="true">
    <defs><linearGradient id="heroShade" x1="0" x2="1"><stop offset="0" stop-color="#14215a"/><stop offset="1" stop-color="#14215a" stop-opacity=".85"/></linearGradient></defs>
    <polygon points="0,0 640,0 540,520 0,520" fill="url(#heroShade)"/>
    <polygon points="540,520 1200,420 1200,520" fill="#14215a"/>
  </svg>
  <div class="abs hero-kicker">BUY LIKE A FLEET</div>
  <h1 class="abs hero-title">SAVE THOUSANDS</h1>
  <a class="abs btn btn-ghost hero-inv" href="#" style="font-size:13px">See Our Inventory</a>
  <div class="abs hero-phone">
    <svg width="28" height="28" viewBox="0 0 28 28"><circle cx="14" cy="14" r="13" fill="#0054AA"/><path d="M10 8l3 3-2 2c1 2 2 3 4 4l2-2 3 3-2 2c-5 0-10-5-10-10z" fill="#fff"/></svg>
    913-555-0142
  </div>
  <div class="abs cats">
    <div class="cat"><div class="cat-photo" role="img" aria-label="White refrigerated trailer" style="background:linear-gradient(180deg,#cfd6e2,#8e98ad)"></div><div class="cat-label">REEFER TRAILERS <span>›</span></div></div>
    <div class="cat"><div class="cat-photo" role="img" aria-label="Red sleeper cab truck" style="background:linear-gradient(180deg,#9fb6d8,#a23a3e 70%,#555)"></div><div class="cat-label">SLEEPERS <span>›</span></div></div>
    <div class="cat"><div class="cat-photo" role="img" aria-label="White dry van trailer" style="background:linear-gradient(180deg,#b9c7de,#e6e8ee 60%,#8a8f9c)"></div><div class="cat-label">DRY VANS <span>›</span></div></div>
    <div class="cat"><div class="cat-photo" role="img" aria-label="Mobile crane truck" style="background:linear-gradient(180deg,#a7c2e4,#e1e4ea 60%,#7b7f8a)"></div><div class="cat-label">CRANES <span>›</span></div></div>
  </div>
</section>

<div class="abs wholesale-bg"></div>
<div class="abs wholesale-photo" role="img" aria-label="Fleet of white vans lined up"></div>
<div class="abs wholesale-text">
  <h2 class="accent-title"><span class="sq"></span><span class="first">W</span>HOLESALE<br>REEFERS, DRY VANS,<br>&amp; SLEEPERS</h2>
  <p>Brelvon Truck &amp; Trailer is an equipment dealership in Kansas City, offering wholesale reefers, dry vans, and sleepers at the best prices. We aren't a normal dealership, because you can buy directly from us at wholesale price and save thousands. We don't have a fancy sales lot, but we do have the lowest prices on good, clean equipment in the country.</p>
</div>
<a class="abs btn btn-navy wholesale-btn" href="#">Learn More</a>

<div class="abs buying-head"><h2 class="accent-title"><span class="sq"></span><span class="first">B</span>UYING FROM BRELVON TRUCK<br>&amp; TRAILER</h2></div>
<p class="abs buying-lead">When you buy from Brelvon, you are buying at a "wholesale price." In other words, you pay the same price a truck dealer pays when they buy from us. We guarantee that you won't find a better price on the same truck or trailer anywhere in the U.S.</p>
<h3 class="abs why-title">HOW ARE THE PRICES SO LOW?</h3>
<div class="abs why-list">
  <div class="why-item"><div class="why-icon"><svg width="32" height="24" viewBox="0 0 32 24"><rect x="1" y="4" width="18" height="12" fill="none" stroke="#fff" stroke-width="2"/><path d="M19 8h6l5 5v3H19z" fill="none" stroke="#fff" stroke-width="2"/><circle cx="7" cy="19" r="3" fill="#fff"/><circle cx="25" cy="19" r="3" fill="#fff"/></svg></div><div class="why-box">We buy huge packages of equipment, 100+ at a time, so we get a great price on what we buy.</div></div>
  <div class="why-item"><div class="why-icon"><svg width="28" height="28" viewBox="0 0 28 28"><rect x="2" y="2" width="24" height="24" fill="none" stroke="#fff" stroke-width="2"/><path d="M7 7l14 14M21 7L7 21" stroke="#fff" stroke-width="2"/></svg></div><div class="why-box">We don't operate a big retail sales lot, so we don't have all that overhead cost.</div></div>
  <div class="why-item"><div class="why-icon"><svg width="28" height="28" viewBox="0 0 28 28"><circle cx="14" cy="14" r="12" fill="none" stroke="#fff" stroke-width="2"/><text x="14" y="20" text-anchor="middle" font-family="Montserrat,sans-serif" font-weight="700" font-size="16" fill="#fff">$</text></svg></div><div class="why-box">We sell at a lower profit margin, and make it up by selling a lot more equipment.</div></div>
</div>
<div class="abs buying-photo" role="img" aria-label="Two white semi trucks at sunset"></div>
<div class="abs mission"><p>As one of the leading equipment dealerships in the U.S., Brelvon Truck &amp; Trailer is committed to going the extra mile. We believe that offering the best quality equipment at the lowest prices isn't enough. We strive to exceed your expectations by providing the highest level of service from start to finish—no sales talk or runaround.</p></div>

<div class="abs sell-band" role="img" aria-label="Row of trucks parked under a blue sky"></div>
<h2 class="abs sell-title">Have more<br>equipment than<br>you need?</h2>
<a class="abs btn btn-ghost sell-btn" href="#">Sell Your Equipment</a>

<div class="abs res-head"><h2 class="accent-title"><span class="sq"></span><span class="first">R</span>ESOURCES</h2></div>
<div class="abs res-arrow" style="left:108px"><svg width="16" height="16" viewBox="0 0 16 16"><path d="M11 2L5 8l6 6" fill="none" stroke="#14215a" stroke-width="2.5"/></svg></div>
<div class="abs res-cards">
  <article class="res-card"><div class="res-photo" role="img" aria-label="Blue trucks lined up at a yard" style="background:linear-gradient(160deg,#3b66b5,#9db4d8 60%,#5a6278)"></div><h3>Save big: learn to buy trucks wholesale</h3></article>
  <article class="res-card"><div class="res-photo" role="img" aria-label="Close-up of truck tires" style="background:linear-gradient(160deg,#2c2f38,#6b7080 55%,#b7bcc7)"></div><h3>Transform your trucking experience with an APU!</h3></article>
  <article class="res-card"><div class="res-photo" role="img" aria-label="Semi truck on a highway at dusk" style="background:linear-gradient(160deg,#1f2b58,#5b6f9c 55%,#c7a67c)"></div><h3>Why Ridgeline Haulmaster's are the better choice</h3></article>
</div>
<div class="abs res-arrow" style="left:1036px"><svg width="16" height="16" viewBox="0 0 16 16"><path d="M5 2l6 6-6 6" fill="none" stroke="#14215a" stroke-width="2.5"/></svg></div>

<div class="abs contact-bg"></div>
<div class="abs contact-head">
  <h2 class="accent-title"><span class="sq"></span><span class="first">Q</span>UESTIONS<br>ABOUT A TRUCK<br>OR TRAILER?</h2>
  <p>Have a question about pricing, availability, or a specific unit? Send us a message and we'll get back to you quickly.</p>
</div>
<div class="abs contact-line" style="top:4356px"><div class="ico"><svg width="18" height="18" viewBox="0 0 18 18"><path d="M4 2l3 3-2 2c1 2 3 4 5 5l2-2 3 3-2 2C7 15 3 11 2 4z" fill="#14215a"/></svg></div><div><small>PHONE</small><strong>913-555-0142</strong></div></div>
<div class="abs contact-line" style="top:4424px"><div class="ico"><svg width="18" height="14" viewBox="0 0 18 14"><rect x="1" y="1" width="16" height="12" fill="none" stroke="#14215a" stroke-width="2"/><path d="M1 1l8 7 8-7" fill="none" stroke="#14215a" stroke-width="2"/></svg></div><div><small>EMAIL</small><strong style="font-size:16px">info@brelvon.com</strong></div></div>

<form class="abs form-card">
  <h3>SEND A MESSAGE</h3>
  <div class="field-row"><div class="field"><i></i>Full Name</div><div class="field"><i></i>Business Name</div></div>
  <div class="field-row"><div class="field"><i></i>Email Address</div></div>
  <div class="field-row"><div class="field"><i></i>Phone No.</div></div>
  <div class="field-row"><div class="field"><i></i>Phone No.</div></div>
  <a class="btn btn-navy form-btn" href="#">Learn More</a>
</form>

<footer class="abs site-footer"></footer>
<div class="abs brand foot-brand"><span class="name" style="font-size:44px">BRELVON</span><span class="sub" style="font-size:21px">Truck &amp; Trailer</span></div>
<nav class="abs foot-nav"><a href="#">Sleepers</a><a href="#">Reefers</a><a href="#">Dry Vans</a><a href="#">Cranes</a><a href="#">Resources</a><a href="#">Contact</a></nav>
<div class="abs foot-rule"></div>
<div class="abs social"><span></span><span></span></div>
<div class="abs copy">Copyright 2026 Brelvon</div>
<div class="abs policy">Privacy Policy</div>

</body>
</html>
```